Personal coach needs brochure design for inspirational essay about authenticity

Overview:
I want a beautiful brochure, 11”x17” that folds to 8-1/2”x11” with 4 pages. Think of it as an oversize greeting card.
• Front cover: photograph of a dancer and title with attribution of quote (Lumafold jpeg photo attached)
• Inside spread: Copy (Helena Brisk copy attached) with some appropriate illustration, based on cover photo
• Back cover: contact information, brief descriptive copy, two small photos (jpeg photo attached; see copy for direction)
Copy for front cover title, inside spread and back cover is attached in doc titled "Helena Brisk copy"

Purpose of brochure:
I'm a personal coach and once a year I produce a 4-page illustrated inspirational essay, which invites personal reflection on living a more mindful, meaningful life. Most people I send them to collect them. Someday in the future I'd like to put a collection of these essays into a coffee table book and also create a website for the collection, which is related to the personal coaching that I do.
I have the brochures printed hard copy. I have attached a few examples from previous years. Each has a unique design related to its theme.

Concept:
This year’s essay theme, “There will only ever be one you!” is based on a quote by Helena Brisk, a famous modern dancer. The complete quote, which appears in the copy, is about being true to one’s authentic self. The essay is not about dance, but because the author of the quote was a dancer who personified this theme of being unique to self, I have selected a photo of dance for the cover.

Design Guidance:
Front cover: One possibility is to expand the background color of the Lumafold photo so the photo seems to emerge from the background. But I am open to ideas. I think the photo is artsy enough as it is, but there may be other ways to treat it (e.g. special effects) that would also work. The title should appear somewhere. Make the attribution (--Helena Brisk) in smaller type than the title.

Inside Spread: There may be ways to borrow a design motif from the cover photo to make the inside spread more visually interesting, i.e., not just straight copy. I think it may be helpful to make the font size of the quote larger than the rest of the copy, but it has to be read in sequence. Or maybe it's printed in same size as copy, but then also repeated and displayed by itself in larger type.

Back cover: If you look at some of the other examples I’ve sent, you’ll see how the back cover is typically handled. I want a reduced version of the cover to be placed near the line that says "this is the 16th in a series.." Then, there’s a jpeg photo of Helena Brisk that should be placed next to the copy description of her.

Need extra days to review

```html
<!DOCTYPE html>
<html lang="en">
<head>
<meta charset="utf-8">
<title>There Will Only Ever Be One You – Brochure</title>
<link rel="stylesheet" href="https://fonts.googleapis.com/css2?family=Playfair+Display:ital,wght@1,500&family=Poppins:wght@400;600&family=Great+Vibes&family=Montserrat:wght@500&display=swap">
<style>
:root{
  --paper:#ffffff;
  --ink-dark:#0b0b0b;
  --smoke-1:#3a3b3d;
  --smoke-2:#1a1a1b;
  --text-light:#f2f2f2;
  --text-muted:#a8a8a8;
  --rule:#d8d8d8;
  --photo-a:#4a5663;
  --photo-b:#23272c;
}
*{box-sizing:border-box;margin:0;padding:0}
html,body{width:685px;height:1200px;overflow:hidden;background:var(--paper)}
body{position:relative;font-family:"Poppins",sans-serif;color:var(--text-light)}

.spread{position:absolute;left:20px;width:645px;height:418px;box-shadow:0 4px 14px rgba(0,0,0,.35);overflow:hidden}
.spread--outer{top:150px;background:radial-gradient(ellipse at 70% 40%,var(--smoke-1),var(--smoke-2) 75%)}
.spread--inner{top:632px;background:var(--ink-dark)}
.page{position:absolute;top:0;width:322.5px;height:418px}
.page--left{left:0}
.page--right{left:322.5px}
.page-frame{position:absolute;inset:8px;border:1px solid var(--rule);pointer-events:none}
.page--left .page-frame{right:0}
.page--right .page-frame{left:0}

/* back cover */
.series-intro{position:absolute;left:19px;top:20px;width:205px;font-size:8.6px;line-height:10.8px}
.series-intro strong{font-weight:600}
.signature{position:absolute;right:22px;top:70px;font-family:"Great Vibes",cursive;font-size:13px;color:var(--text-light)}
.feature-box{position:absolute;left:79px;top:95px;width:222px;height:108px;border:1px solid var(--rule)}
.feature-photo{position:absolute;left:20px;top:113px;width:114px;height:84px;border:1px solid var(--rule);background:linear-gradient(135deg,#2d2d2d,#595552 55%,#1c1c1c)}
.feature-caption{position:absolute;left:169px;top:124px;width:122px;font-weight:600;font-size:9.4px;line-height:11.5px}
.qmark{position:absolute;font-family:"Playfair Display",serif;font-style:italic;font-size:26px;line-height:1;color:var(--text-light)}
.connector{position:absolute;background:var(--rule)}
.dot{position:absolute;width:4px;height:4px;border-radius:50%;background:var(--text-light)}
.bio{position:absolute;top:216px;height:140px;overflow:hidden;font-size:5.3px;line-height:7.4px;text-align:justify;hyphens:auto}
.bio b{font-weight:600}
.bio--subject{left:20px;width:137px}
.bio--photographer{left:168px;width:134px}
.studio-name{position:absolute;left:20px;top:364px;font-weight:600;font-size:12px}
.studio-address{position:absolute;left:20px;top:381px;font-size:7px;line-height:12px}
.studio-contact{position:absolute;left:183px;top:381px;font-size:7px;line-height:12px}
.contact-row{display:flex;align-items:center;gap:6px}
.contact-row svg{width:8px;height:8px}

/* front cover */
.cover-title{position:absolute;left:20px;top:22px;font-family:"Playfair Display",serif;font-style:italic;font-weight:500;font-size:28px;line-height:30px;letter-spacing:.5px;text-transform:uppercase}
.cover-title .muted{color:var(--text-muted)}
.cover-photo{position:absolute;left:10px;top:98px;width:300px;height:282px;background:radial-gradient(ellipse 55% 50% at 55% 50%,var(--photo-a),var(--photo-b) 70%,transparent 100%)}
.cover-author{position:absolute;left:42px;top:380px;font-family:"Montserrat",sans-serif;font-weight:500;font-size:13px;letter-spacing:5px;text-transform:uppercase}

/* inside spread */
.essay-block{position:absolute;font-size:6.6px;line-height:8.7px;text-align:justify}
.essay-block p{padding:0}
.essay-block--wide{left:13px;width:288px;border-top:1px dashed var(--rule);border-bottom:1px dashed var(--rule);border-right:1px dashed var(--rule);padding:10px 6px 8px}
.essay-block--inset{left:39px;width:262px;border-top:1px dashed var(--rule);border-bottom:1px dashed var(--rule);border-left:1px dashed var(--rule);padding:9px 6px 8px 17px}
.quote-frame{position:absolute;left:22px;top:25px;width:281px;height:261px;border:1px solid var(--rule)}
.quote-text{position:absolute;left:35px;top:36px;width:256px;font-family:"Great Vibes",cursive;font-size:14.6px;line-height:17.2px;text-align:justify}
.quote-mark-bg{position:absolute;background:var(--ink-dark);padding:0 5px}
.reflection{position:absolute;left:18px;width:290px;font-size:6.4px;line-height:7.8px;text-align:justify}
</style>
</head>
<body>

<!-- Outer spread: back cover + front cover -->
<section class="spread spread--outer" aria-label="Outer spread">
  <div class="page page--left">
    <div class="page-frame"></div>
    <p class="series-intro"><strong>There Will Only Ever Be One You</strong> is the 16th in a series of Labor Day essays inviting a moment of reflection on living a more meaningful, more mindful life</p>
    <p class="signature">Nora Whitcombe, Ph.D.</p>

    <div class="connector" style="left:79px;top:91px;width:1px;height:14px"></div>
    <div class="dot" style="left:77px;top:103px"></div>
    <div class="feature-box"></div>
    <div class="feature-photo" role="img" aria-label="Archival black and white photograph of a dancer in a flowing skirt"></div>
    <span class="qmark" style="left:140px;top:112px">“</span>
    <p class="feature-caption">Helena Brisk in Letter to the World, No. 1”© The Clara Vesey Archive</p>
    <span class="qmark" style="left:283px;top:176px">”</span>
    <div class="connector" style="left:79px;top:203px;width:1px;height:6px"></div>
    <div class="dot" style="left:77px;top:207px"></div>

    <p class="bio bio--subject"><b>ABOUT HELENA BRISK:</b> Born in 1894, Helena Brisk danced and taught for over 70 years. She is recognized as a primal artistic force of the 20th century, whose influence on modern dance has been compared to that of the great painters, writers and architects of her age. Her themes dealt with the lives and conflicts of ordinary people, and she brought serious issues to the stage like war, poverty, intolerance and injustice. Rebelling against conventions of the past, her dancing and choreography exposed the depths of human emotion through intense movements that were forceful, stark, angular, jagged and percussive – startlingly unlike the formality of classical ballet, which she saw as antiquated.</p>
    <p class="bio bio--photographer"><b>About Photographer Clara Vesey:</b> In 1935 Clara Vesey saw a performance by modern dancer and choreographer Helena Brisk. Vesey was so inspired by the dance performance that she introduced herself to Brisk, and the two artists began an artistic collaboration that lasted more than 60 years. Vesey often photographed dancers in action, to capture the emotion behind their movement. Her artistic style was in line with Brisk's philosophy of dance. This photo from the dance, "Letter to the World," is one of Vesey's most famous photographs. The title of this work comes from a poem by a New England poet, which inspired Brisk to create a dance based on the poet's life.</p>

    <p class="studio-name">Heron Hill House</p>
    <p class="studio-address">18 Orchard Lane<br>Linden Falls, Vermont&nbsp; 05099</p>
    <div class="studio-contact">
      <div class="contact-row">
        <svg viewBox="0 0 16 16" aria-hidden="true"><circle cx="8" cy="8" r="7.3" fill="none" stroke="#f2f2f2" stroke-width="1.4"/><path d="M5.2 4.3l1.4-.2.8 2-1 .8c.5 1.1 1.4 2 2.5 2.5l.8-1 2 .8-.2 1.4c-3.5.2-6.5-2.8-6.3-6.3z" fill="#f2f2f2"/></svg>
        <span>555-013-4827</span>
      </div>
      <div class="contact-row">
        <svg viewBox="0 0 16 16" aria-hidden="true"><circle cx="8" cy="8" r="7.3" fill="none" stroke="#f2f2f2" stroke-width="1.4"/><rect x="4" y="5.2" width="8" height="5.6" fill="none" stroke="#f2f2f2" stroke-width="1.1"/><path d="M4 5.4l4 3 4-3" fill="none" stroke="#f2f2f2" stroke-width="1.1"/></svg>
        <span>nora@whitcombe.example</span>
      </div>
    </div>
  </div>

  <div class="page page--right">
    <div class="page-frame"></div>
    <div class="cover-photo" role="img" aria-label="Photograph of a dancer leaping mid-air in a flowing dark grey dress against a smoky background"></div>
    <h1 class="cover-title">There will<br><span class="muted">only ever</span><br>be one you!</h1>
    <p class="cover-author">Helena&nbsp; Brisk</p>
  </div>
</section>

<!-- Inside spread: essay + quote -->
<section class="spread spread--inner" aria-label="Inside spread">
  <div class="page page--left">
    <div class="page-frame"></div>

    <div class="essay-block essay-block--wide" style="top:17px">
      <p>In the rural Ohio village where I grew up, one of the highlights of Sunday morning church service -- in between congregational hymn-singing and the preacher's sermon -- was the “special selection,” a musical performance by a parishioner. Typically, it was a vocalist or instrumental on piano, organ or violin. One Sunday, we were surprised by an unusual performance. A plump, buxom farm wife approached the pulpit, puckered up her lips and unexpectedly began to whistle the hymn “The Old Rugged Cross.” As a 10-year-old, I found this hilarious as I tried to choke back my wide-eyed amazement and giggles.</p>
    </div>
    <div class="dot" style="left:77px;top:15px"></div>

    <div class="essay-block essay-block--inset" style="top:126px">
      <p>Despite the irreverence of my pre-adolescent reaction, this memory has stayed with me for decades as an iconic example of the wonderment of individual differences. Of the delight I find in witnessing someone express herself in sometimes surprising and even courageous ways. Of the marvel of beholding a person be truly authentic and uniquely original.</p>
    </div>
    <div class="dot" style="left:270px;top:196px"></div>

    <div class="essay-block essay-block--wide" style="top:208px">
      <p>Someone who personified the irrepressible impulse to express her individuality was the early 20th century dancer and choreographer Helena Brisk. A pioneer of modern dance, she threw tradition overboard and was inspired to dance in a way that was a radical departure from the formalized style and rigidly dictated forms of classical ballet. Brisk felt compelled to express the rawness and emotion of human experience in her dancing -- not just present a form of pretty entertainment. Iconoclastically brilliant, she created a new language of dance, a revolutionary vocabulary of movement that electrified the stage, often creating a visceral response in the audience.</p>
    </div>
    <div class="dot" style="left:270px;top:206px"></div>

    <div class="essay-block essay-block--inset" style="top:321px">
      <p>In her biography of Brisk, her friend and equally talented choreographer Irene Dalloway recalled that despite sensational reviews for her own innovative work in the Broadway musical Prairie Lights, Dalloway had a gnawing feeling that her work was only mediocre. Dalloway confessed her anxieties to Brisk who listened quietly and then responded, “There will only ever be one you!”</p>
    </div>
    <div class="dot" style="left:270px;top:386px"></div>
  </div>

  <div class="page page--right">
    <div class="page-frame"></div>
    <div class="quote-frame"></div>
    <span class="qmark quote-mark-bg" style="left:141px;top:12px">“</span>
    <p class="quote-text">There is a vitality, a life force, an energy, a quickening that is translated through you into action. And because there is only one of you in all of time, this expression is unique. And if you block it, the world will not have it. It is not your business to determine how good it is nor how valuable nor how it compares with other expressions. It is your business to keep it yours clearly and directly, to keep the channel open. You have to keep open and aware directly to the urges that motivate you. Above all else, keep the channel open.</p>
    <span class="qmark quote-mark-bg" style="left:141px;top:276px">”</span>

    <p class="reflection" style="top:302px">Brisk's wisdom reminds us that we must not hold back or judge our gifts. Although there may be moments when we doubt ourselves or when we worry that we're not good enough, our job is to be fearless and to “keep the channel open.”</p>
    <p class="reflection" style="top:341px">Guard the precious miracle of your own uniqueness. Find that home-sweet-home feeling where you feel you are your most authentic self. There will only ever be one you! And importantly, respect the differences of others. Our world would be a drab, boring place if we all only whistled one tune.</p>
  </div>
</section>

</body>
</html>
```